Visitenkarten-Design für Fachärztin für Allgemeinmedizin
Zielgruppe
Visitenkarte passend zum Logo mit folgenden Daten:
Dr. med Miriam Valdorf
Fachärztin für Allgemeinmedizin
Brennwaldweg 14
72946 Eichenfurt OT Talgrund
Telefon 07451/8194
Website: www.hausarztpraxis-talgrund.de
Online Terminvereinbarung
Sprechstunde
Mo 8-11:30Uhr sowie 14-17 Uhr
Die 8-13 Uhr
Mi 8-13 Uhr
Do 8-11:30uhr sowie 14-18 Uhr
Fr 8- 11:30Uhr
Sowie nach Vereinbarung
Laborzeiten tägl. 7:15 -8 Uhr
Telefonzeiten tägl. 8-11 Uhr , sowie Mo und Fr 14-16 Uhr
Aufgabenstellung
Nach dem Logo, welches hier erstellt wurde Visitenkarten ..
vorher und Rückseite!
Sprechzeiten, Name, Adresse , Tele Fax und Website
In den Farben des Magenta und Grau

```html
<!DOCTYPE html>
<html lang="de">
<head>
<meta charset="utf-8">
<title>Visitenkarten Hausarztpraxis</title>
<link rel="stylesheet" href="https://fonts.googleapis.com/css2?family=Cinzel:wght@500;600&family=Montserrat:wght@500;600;700&family=Open+Sans:wght@400;600;700&display=swap">
<style>
  :root {
    --magenta: #c2185b;
    --grey: #4a4f55;
    --grey-light: #6b7076;
    --paper: #ffffff;
    --stage: #d9d9d9;
  }
  * { box-sizing: border-box; margin: 0; padding: 0; }
  html, body { width: 1200px; height: 900px; overflow: hidden; }
  body {
    background: radial-gradient(circle at 50% 40%, #ececec, var(--stage) 75%);
    display: flex; flex-direction: column; align-items: center; justify-content: center;
    gap: 36px;
  }
  .card {
    position: relative; width: 620px; height: 400px; background: var(--paper);
    box-shadow: 0 10px 28px rgba(0,0,0,.18); overflow: hidden;
  }

  /* Front */
  .front { font-family: "Open Sans", sans-serif; color: var(--grey); }
  .front .doctor { position: absolute; left: 44px; top: 40px; width: 300px; }
  .front .doctor-name { font-size: 25px; font-weight: 700; color: var(--magenta); white-space: nowrap; }
  .front .doctor-title { font-size: 13px; font-weight: 600; color: var(--grey-light); margin-top: 2px; }
  .front .divider { width: 270px; height: 2px; background: var(--magenta); margin-top: 14px; }
  .front .contact { margin-top: 14px; font-size: 15px; line-height: 22px; }
  .front .hotline { font-weight: 700; color: var(--magenta); font-size: 15px; }
  .front .line { display: flex; align-items: center; gap: 8px; }
  .front .line svg { width: 14px; height: 14px; fill: var(--magenta); }
  .front .address { margin-top: 8px; }
  .front .practice-label {
    position: absolute; right: 48px; top: 150px; font-family: "Cinzel", serif;
    font-size: 26px; font-weight: 600; letter-spacing: 1px; color: var(--magenta);
  }
  .front .practice-mark {
    position: absolute; right: 48px; top: 222px; display: flex; align-items: center; gap: 12px;
  }
  .mark-dot { width: 30px; height: 30px; border-radius: 50%; border: 3px solid var(--magenta); flex: none; }
  .front .practice-mark span { font-size: 19px; font-weight: 700; color: var(--magenta); }
  .front .band {
    position: absolute; left: 0; right: 0; bottom: 0; height: 60px; background: var(--magenta);
    display: flex; align-items: center; justify-content: space-between; padding: 0 44px;
    color: #fff; font-size: 16px;
  }

  /* Back */
  .back { font-family: "Montserrat", sans-serif; }
  .back .header {
    height: 130px; display: flex; align-items: center; justify-content: center; gap: 14px;
  }
  .back .header span { font-size: 21px; font-weight: 600; color: var(--magenta); letter-spacing: 1px; }
  .back .hours {
    position: absolute; left: 0; right: 0; bottom: 0; height: 270px; background: var(--magenta);
    color: #fff; display: grid; grid-template-columns: 1fr 1fr; gap: 30px; padding: 30px 40px;
  }
  .back h2 { font-size: 15px; font-weight: 700; text-transform: uppercase; margin-bottom: 6px; }
  .back .schedule { font-size: 14px; font-weight: 500; line-height: 21px; list-style: none; }
  .back .note { font-size: 13px; font-weight: 700; text-transform: uppercase; margin-top: 18px; }
  .back .times p { font-size: 13px; font-weight: 700; text-transform: uppercase; line-height: 20px; margin-bottom: 28px; }
</style>
</head>
<body>

  <section class="card front">
    <div class="doctor">
      <h1 class="doctor-name">Dr. med. Miriam Valdorf</h1>
      <p class="doctor-title">Fachärztin für Allgemeinmedizin</p>
      <div class="divider"></div>
      <div class="contact">
        <p class="hotline">REZEPTHOTLINE</p>
        <p class="line">
          <svg viewBox="0 0 24 24" aria-hidden="true"><path d="M6.6 10.8a15 15 0 0 0 6.6 6.6l2.2-2.2a1 1 0 0 1 1-.25 11.4 11.4 0 0 0 3.6.57 1 1 0 0 1 1 1V20a1 1 0 0 1-1 1A17 17 0 0 1 3 4a1 1 0 0 1 1-1h3.5a1 1 0 0 1 1 1c0 1.25.2 2.450.57 3.57a1 1 0 0 1-.25 1z"/></svg>
          07451/8194
        </p>
        <p class="line">
          <svg viewBox="0 0 24 24" aria-hidden="true"><path d="M6 2h10v6H6zM3 9h18v9h-3v4H6v-4H3zm5 6v5h8v-5z"/></svg>
          07451/8195
        </p>
        <p class="address">Brennwaldweg 14<br>72946 Eichenfurt OT Talgrund</p>
      </div>
    </div>

    <p class="practice-label">HAUSARZTPRAXIS</p>
    <div class="practice-mark">
      <div class="mark-dot"></div>
      <span>Praxis Valdorf</span>
    </div>

    <footer class="band">
      <span class="website">www.hausarztpraxis-talgrund.de</span>
      <span class="booking">Online Terminvereinbarung</span>
    </footer>
  </section>

  <section class="card back">
    <header class="header">
      <div class="mark-dot"></div>
      <span>Dr. med. Miriam Valdorf</span>
    </header>
    <div class="hours">
      <div class="consulting">
        <h2>Sprechstunde</h2>
        <ul class="schedule">
          <li>Mo 8–11:30 Uhr sowie 14–17 Uhr</li>
          <li>Die 8–13 Uhr</li>
          <li>Mi 8–13 Uhr</li>
          <li>Do 8–11:30 Uhr sowie 14–18 Uhr</li>
          <li>Fr 8–11:30 Uhr</li>
        </ul>
        <p class="note">Sowie nach Vereinbarung</p>
      </div>
      <div class="times">
        <p>Laborzeiten tägl. 7:15 – 8 Uhr</p>
        <p>Telefonzeiten tägl. 8–11 Uhr,<br>sowie Mo und Fr 14–16 Uhr</p>
      </div>
    </div>
  </section>

</body>
</html>
```